Flyer for local business that installs fences and sells fence materials

We recently began selling fence materials, in addition to also doing fence installations. We need a flyer that displays our business information and photos of our work, as well as a flyer that shows customers they have the option to buy materials only also.

If they are looking to build a fence - we can help by installing it, or if they want to install themselves, they can buy the materials only from us too. We provide a lifetime warranty on all materials and installations. More information about the company is here: www.BrambleRailWorks.com

Its important to have the company logo, phone number, email and business hours listed (Monday - Thursday 9AM - 3PM, Friday 9AM - 1PM).

It is also important to show the fence material types we offer:
Wood, Chainlink, Vinyl and Aluminum
Updates

Updated with more photos and url to website www.bramblerailworks.com for details

Target Market(s)

Residential Homeowners

Industry/Entity Type

Construction

Font styles to use
Sans Serif
Other font styles liked:
• Arial

Colors
0054AA
0677BA
7BADD7
CADEEF
E8F1F8

Requirements
Must have
• Photos of the fencing we offer
Nice to have
• A way to explain to customers they can hire us to install, or just buy the materials from us
Should not have
• Too many colors or too many words

```html
<!DOCTYPE html>
<html lang="en">
<head>
<meta charset="utf-8">
<title>Bramble Rail Works – Fence Flyer</title>
<link href="https://fonts.googleapis.com/css2?family=Exo+2:ital,wght@0,600;0,700;0,800;1,500&family=Oswald:wght@600&family=Catamaran:wght@400;500;600;700&display=swap" rel="stylesheet">
<style>
  :root{
    --blue:#1f74bf;
    --blue-deep:#0054AA;
    --blue-mid:#0677BA;
    --blue-soft:#7BADD7;
    --blue-pale:#CADEEF;
    --ink:#1d1d1d;
    --wood-light:#efe5d4;
    --wood-mid:#dccbad;
    --white:#ffffff;
  }
  *{box-sizing:border-box;margin:0;padding:0}
  html,body{width:740px;height:1200px;overflow:hidden;background:var(--white)}
  .flyer{position:relative;width:740px;height:1200px;font-family:"Catamaran",Arial,sans-serif;color:var(--ink)}

  /* header */
  .header{position:absolute;left:0;top:0;width:740px;height:154px;background:var(--white)}
  .header-panel{position:absolute;right:0;top:0;width:360px;height:154px}
  .brand{position:absolute;left:38px;top:30px;display:flex;align-items:center;gap:12px}
  .brand-mark{width:58px;height:58px;background:var(--blue-deep)}
  .brand-text{display:flex;flex-direction:column}
  .brand-name{font-family:"Exo 2",Arial,sans-serif;font-weight:700;font-size:27px;color:var(--blue);line-height:1.05}
  .brand-phone{font-family:"Exo 2",Arial,sans-serif;font-weight:800;font-size:29px;color:#231f20;line-height:1.1;letter-spacing:.5px}
  .brand-tagline{position:absolute;left:136px;top:118px;font-family:"Exo 2",Arial,sans-serif;font-weight:600;font-size:10.5px;color:#231f20}
  .contact{position:absolute;left:418px;top:22px;color:var(--white)}
  .contact-title{font-family:"Exo 2",Arial,sans-serif;font-weight:600;font-size:17px}
  .contact-sub{font-family:"Exo 2",Arial,sans-serif;font-style:italic;font-weight:500;font-size:15px;margin-left:4px}
  .contact-line{display:flex;align-items:center;gap:6px;font-family:"Exo 2",Arial,sans-serif;font-weight:600;font-size:15.5px;margin-top:4px;margin-left:10px}
  .contact-line.small{font-size:13.5px;font-weight:500;margin-left:16px}

  /* hero */
  .hero-photo{position:absolute;left:0;top:154px;width:740px;height:454px;
    background:linear-gradient(160deg,#5b7a3d 0%,#7c8f4e 30%,#cdb487 55%,#e6d2a8 70%,#5f7a3a 100%)}
  .badge{position:absolute;left:528px;top:384px;width:178px;height:178px;border-radius:50%;
    background:var(--blue);border:5px solid var(--white);box-shadow:0 0 0 3px var(--blue);
    display:flex;align-items:center;justify-content:center;text-align:center;
    color:var(--white);font-weight:600;font-size:15.5px;line-height:1.18;padding:18px}

  /* banner */
  .banner{position:absolute;left:0;top:608px;width:740px;height:120px;background:var(--blue);color:var(--white);text-align:center}
  .banner-headline{font-family:"Oswald",Arial,sans-serif;font-weight:600;font-size:40px;letter-spacing:-.3px;line-height:1;margin-top:16px;transform:scaleX(.88)}
  .banner-sub{font-family:"Catamaran",Arial,sans-serif;font-weight:500;font-size:27px;line-height:1;margin-top:12px;letter-spacing:.3px}

  /* features */
  .features{position:absolute;left:0;top:728px;width:740px;height:392px;
    background:linear-gradient(90deg,var(--wood-light) 0%,#e6d8bf 40%,var(--wood-mid) 100%)}
  .benefits{position:absolute;left:44px;top:16px;list-style:none}
  .benefits li{display:flex;align-items:center;gap:7px;font-size:17px;font-weight:500;color:#2b2b2b;height:31.5px}
  .benefits .note{position:absolute;left:22px;top:250px;font-size:10.5px;color:#555}
  .estimates{position:absolute;left:0;top:296px;width:345px;height:96px;background:rgba(255,255,255,.78);padding:10px 0 0 44px}
  .estimates h3{font-family:"Exo 2",Arial,sans-serif;font-weight:800;font-size:13.5px;color:var(--blue)}
  .estimates p{font-size:11px;line-height:1.25;color:#222;font-weight:500;width:290px}
  .work-photo{position:absolute;border:2px solid var(--white);box-shadow:0 1px 3px rgba(0,0,0,.25)}
  .work-vinyl{left:351px;top:12px;width:166px;height:117px;background:linear-gradient(180deg,#6d9ad4 0%,#e9edf0 45%,#f7f7f4 65%,#6f8a44 100%)}
  .work-wood{left:529px;top:12px;width:166px;height:117px;background:linear-gradient(180deg,#5e8fcf 0%,#c9a576 30%,#d8b687 75%,#7b8a4a 100%)}
  .work-chain{left:351px;top:145px;width:344px;height:231px;background:linear-gradient(170deg,#9cb0c6 0%,#b9b9a8 30%,#889263 55%,#6f7d45 100%)}

  /* footer */
  .footer{position:absolute;left:0;top:1120px;width:740px;height:80px;background:var(--blue);color:var(--white)}
  .footer-divider{position:absolute;left:336px;top:0;width:6px;height:80px;background:var(--white);transform:skewX(-8deg)}
  .hours{position:absolute;left:44px;top:16px;font-family:"Exo 2",Arial,sans-serif;font-weight:700}
  .hours-title{font-size:15px;color:var(--blue-pale)}
  .hours-time{font-size:15.5px}
  .online{position:absolute;left:368px;top:16px;font-family:"Exo 2",Arial,sans-serif;font-weight:600;font-size:16px}
  .online div{display:flex;align-items:center;gap:7px;height:24px}
</style>
</head>
<body>
<main class="flyer">

  <header class="header">
    <svg class="header-panel" viewBox="0 0 360 154" aria-hidden="true">
      <polygon points="22,0 360,0 360,154 0,154" fill="var(--blue-mid)"/>
      <polygon points="10,0 22,0 0,154 -12,154" fill="var(--blue-soft)"/>
      <polygon points="34,0 360,0 360,154 12,154" fill="var(--blue)"/>
    </svg>
    <div class="brand">
      <span class="brand-mark"></span>
      <div class="brand-text">
        <span class="brand-name">Bramble Rail Works</span>
        <span class="brand-phone">555-014-2290</span>
      </div>
    </div>
    <p class="brand-tagline">"Because Good Fences Make Good Neighbors"</p>

    <div class="contact">
      <p class="contact-title">Financing Available!</p>
      <p class="contact-sub">Call or Email us today for a free estimate!</p>
      <p class="contact-line">
        <svg width="15" height="15" viewBox="0 0 16 16" aria-hidden="true"><circle cx="8" cy="8" r="7.2" fill="none" stroke="#fff" stroke-width="1.4"/><path d="M5.2 4.3l1.4-.4.9 2-.9.8c.5 1 1.2 1.7 2.2 2.2l.8-.9 2 .9-.4 1.4c-3.3-.2-5.8-2.7-6-6z" fill="#fff"/></svg>
        555-014-2290
      </p>
      <p class="contact-line small">
        <svg width="14" height="14" viewBox="0 0 16 16" aria-hidden="true"><circle cx="8" cy="8" r="7.2" fill="none" stroke="#fff" stroke-width="1.4"/><path d="M8 3.5a2.8 2.8 0 0 0-2.8 2.8C5.2 8.4 8 12 8 12s2.8-3.6 2.8-5.7A2.8 2.8 0 0 0 8 3.5zm0 3.9a1.1 1.1 0 1 1 0-2.2 1.1 1.1 0 0 1 0 2.2z" fill="#fff"/></svg>
        48 Larkspur Ln, Millbrook NC 28000
      </p>
    </div>
  </header>

  <section class="hero">
    <div class="hero-photo" role="img" aria-label="Photo of an installer nailing pickets onto a long new wooden privacy fence in a grassy yard"></div>
    <p class="badge">Beautiful, professionally Installed fences at affordable prices! Many fence styles available.</p>
  </section>

  <section class="banner">
    <h1 class="banner-headline">WE BUILD FENCES &amp; SELLING FENCE MATERIALS</h1>
    <p class="banner-sub">And we would love to build your fence too!</p>
  </section>

  <section class="features">
    <ul class="benefits">
      <li><svg width="15" height="15" viewBox="0 0 16 16" aria-hidden="true"><circle cx="8" cy="8" r="8" fill="var(--blue)"/><path d="M4.5 8.2l2.3 2.2 4.7-4.8" fill="none" stroke="#fff" stroke-width="1.8"/></svg>Free Estimates</li>
      <li><svg width="15" height="15" viewBox="0 0 16 16" aria-hidden="true"><circle cx="8" cy="8" r="8" fill="var(--blue)"/><path d="M4.5 8.2l2.3 2.2 4.7-4.8" fill="none" stroke="#fff" stroke-width="1.8"/></svg>Professional Installation</li>
      <li><svg width="15" height="15" viewBox="0 0 16 16" aria-hidden="true"><circle cx="8" cy="8" r="8" fill="var(--blue)"/><path d="M4.5 8.2l2.3 2.2 4.7-4.8" fill="none" stroke="#fff" stroke-width="1.8"/></svg>Concrete In EVERY Post</li>
      <li><svg width="15" height="15" viewBox="0 0 16 16" aria-hidden="true"><circle cx="8" cy="8" r="8" fill="var(--blue)"/><path d="M4.5 8.2l2.3 2.2 4.7-4.8" fill="none" stroke="#fff" stroke-width="1.8"/></svg>HOA Submission Assistance</li>
      <li><svg width="15" height="15" viewBox="0 0 16 16" aria-hidden="true"><circle cx="8" cy="8" r="8" fill="var(--blue)"/><path d="M4.5 8.2l2.3 2.2 4.7-4.8" fill="none" stroke="#fff" stroke-width="1.8"/></svg>Lifetime Workmanship Warranty</li>
      <li><svg width="15" height="15" viewBox="0 0 16 16" aria-hidden="true"><circle cx="8" cy="8" r="8" fill="var(--blue)"/><path d="M4.5 8.2l2.3 2.2 4.7-4.8" fill="none" stroke="#fff" stroke-width="1.8"/></svg>Experienced Installation Teams</li>
      <li><svg width="15" height="15" viewBox="0 0 16 16" aria-hidden="true"><circle cx="8" cy="8" r="8" fill="var(--blue)"/><path d="M4.5 8.2l2.3 2.2 4.7-4.8" fill="none" stroke="#fff" stroke-width="1.8"/></svg>Quality Workmanship &amp; Materials</li>
      <li><svg width="15" height="15" viewBox="0 0 16 16" aria-hidden="true"><circle cx="8" cy="8" r="8" fill="var(--blue)"/><path d="M4.5 8.2l2.3 2.2 4.7-4.8" fill="none" stroke="#fff" stroke-width="1.8"/></svg>FREE Gate Adjustments for LIFE</li>
      <li class="note">*some restrictions apply</li>
    </ul>

    <div class="estimates">
      <h3>ESTIMATES ARE ALWAYS FREE</h3>
      <p>Call, email, or message us online to schedule an in-person estimate. If you know your measurements OR have a lot survey, email or call us for a virtual estimate!</p>
    </div>

    <div class="work-photo work-vinyl" role="img" aria-label="Photo of a white vinyl privacy fence along a row of homes"></div>
    <div class="work-photo work-wood" role="img" aria-label="Photo of a wooden privacy fence gate with a company yard sign"></div>
    <div class="work-photo work-chain" role="img" aria-label="Photo of a new chainlink fence running along a sloped lawn"></div>
  </section>

  <footer class="footer">
    <span class="footer-divider"></span>
    <div class="hours">
      <p class="hours-title">OFFICE HOURS:</p>
      <p class="hours-time">Mon - Thu 9AM - 3PM, Fri 9AM - 1PM</p>
    </div>
    <div class="online">
      <div>
        <svg width="14" height="14" viewBox="0 0 16 16" aria-hidden="true"><circle cx="8" cy="8" r="8" fill="var(--blue-pale)"/><rect x="3.5" y="5" width="9" height="6" rx="1" fill="none" stroke="var(--blue)" stroke-width="1.3"/><path d="M3.8 5.4L8 8.6l4.2-3.2" fill="none" stroke="var(--blue)" stroke-width="1.2"/></svg>
        office@bramblerailworks.com
      </div>
      <div>
        <svg width="14" height="14" viewBox="0 0 16 16" aria-hidden="true"><circle cx="8" cy="8" r="8" fill="var(--blue-pale)"/><circle cx="8" cy="8" r="4.6" fill="none" stroke="var(--blue)" stroke-width="1.2"/><path d="M3.4 8h9.2M8 3.4c-2 2.6-2 6.6 0 9.2M8 3.4c2 2.6 2 6.6 0 9.2" fill="none" stroke="var(--blue)" stroke-width="1"/></svg>
        www.bramblerailworks.com
      </div>
    </div>
  </footer>

</main>
</body>
</html>
```